Honey Label for a private beekeeper

I am an "amateur" beekeeper and like to promote and sell my honey. The target group is anyone who likes honey. Task: The label design should basically be an "eye-catcher" and express the high quality of the natural product honey. In the narrower sense, but which should form a unit in the design: The first part is the so-called guaranty; he connects with the glass and tears when first opening the lid. The lock should be about 2 inches wide and 8 inches long, and adorned by the words 'The best of the nature'. In brackets you always find the english translation of the german text for a better understanding. The second part is the product label. For this there are no shape specifications but max. height is 5cm and maximum is 12cm (for 500g jar), but the following must be included in the account: "Please use the following placeholders", "first name last name", "street house number", "post code city name ") as well as the words" 500g "," Best Before Date ", (" Best before "), behind or below please leave blank space for the stamp imprint of the date," Store dry, dark and protected from heat! dry, dark and protected from heat), And - most important - the text: "Finest bee honey" and in new line "from Cologne - Porz (from Cologne - Porz)" as well as the two varieties "Summer Blossom" or "Spring Blossom" ... in the future may be added more varieties. The company logo should be used in a single color, so that the customer can quickly identify the type of honey in the glass. For this purpose, the respective honeysuckle color, in whatever form, dominate the label or a certain area of ​​it. I have uploaded a few labels from the internet that appealed to me about their style, but it's definitely not about making just one copy of one of these labels. Please use the german text on the label, the translation is just for you. Please contact me in case of any further questions or problems with my explanation. I'm looking forward to your designs! As an 'amateur' I run a hobby-beekeeping and want to drive out my evening gown and summer turkey honey. The target group is anyone who likes honey. Task The Etiketten_Design to be designed should basically be an "eye-catcher", have a high recognition value and express the high quality of the natural product honey. In the narrower sense, two independent parts of the label are to be designed, but which should form a unit in the design: The first part is the so-called warranty; he connects the lid with the glass and tears when first opening the lid. The lock should be about 2 cm wide and 8 cm long, and adorned by the saying 'the best of nature'. The second part is the actual product label. For this there are no size and shape specifications, but the following contents must be considered: The data of the beekeeper (please use the following placeholders "first name last name", "street house number", "ZIP place name") and the information "500g", "At least Best before: "(behind or below, please leave white space for the stamp imprint of the date)," dry, dark and protect from heat! ", and - most importantly - the text: finest bee honey (new line) from Cologne - Porz as well the two denominations spring blossom or summer bloom (in the future may be added more varieties). The logo of the company should be used, but it can also be used on the freshly-baked seal (see appendix) Each type of honey (summer blossom and spring blossom) should be associated with a color, so that the customer can quickly identify which type of honey is in the glass. For this, the respective honeysuckle color, in whatever form, should dominate the label or a certain area of ​​it. With regard to a good reproducibility of the labels in large quantities, we ask for the following further requirements to be observed: • Please place text and picture elements with 4mm distance to the label edges. • Please consider the CYMK color scheme. • If you choose multicolored labels, please use a maximum of four colors. • The honeysuckle color of the product label should NOT be found on the warranty seal (because the guarantee applies generally to any honey jar, regardless of the honeys). • The product label should be editable. • The product label should be scalable (for both small 250g glasses and large 500g glasses). The last two points can be ignored if a larger copy with the indication "500g" and a smaller one with the indication "250g" are created per product label. I'm looking forward to your designs!

Target Market(s)

Neighborhood and shops

Colors

Designer to choose colors to be used in the design.

Requirements
Must have
• With regard to the following further requirements: • Please place text and picture elements 4mm from the edges of the labels. • Please consider the CYMK color scheme. • If you choose multicolored labels, please use a maximum of four colors. The honeysuckle color of the product label should not be found on the warranty. • The product label should be editable. • The product label needs to be scalable The "500g" and the smaller "250g" are created by product label.
Should not have
• Please do not use the color gold no transparent labels

```html
<!DOCTYPE html>
<html lang="de">
<head>
<meta charset="utf-8">
<title>Honig-Etikett Spring Blosom</title>
<link rel="stylesheet" href="https://fonts.googleapis.com/css2?family=PT+Sans+Narrow:wght@700&family=Open+Sans:wght@400&family=PT+Sans:wght@700&display=swap">
<style>
  :root {
    --honey-blue: #009fe3;
    --honey-yellow: #fcc200;
    --ink: #111111;
    --paper: #ffffff;
  }
  * { margin: 0; padding: 0; box-sizing: border-box; }
  html, body { width: 1200px; height: 801px; overflow: hidden; background: var(--paper); }
  .canvas { position: relative; width: 1200px; height: 801px; font-family: "PT Sans Narrow", sans-serif; font-weight: 700; color: var(--ink); }

  /* Guarantee seal */
  .seal { position: absolute; left: 218px; top: 18px; width: 800px; height: 200px; background: var(--honey-blue); }
  .seal-brand { position: absolute; top: 72px; width: 124px; text-align: center; color: var(--honey-yellow); font-size: 20px; line-height: 1.1; letter-spacing: 1px; }
  .seal-brand--left { left: 48px; }
  .seal-brand--right { right: 48px; }
  .seal-text { position: absolute; left: 0; right: 0; top: 44px; text-align: center; font-size: 42px; line-height: 52px; letter-spacing: 0.5px; }

  /* Product label */
  .label { position: absolute; left: 0; top: 266px; width: 1200px; height: 535px; background: var(--honey-blue); overflow: hidden; }
  .best-before { position: absolute; left: 0; width: 1224px; top: 30px; text-align: center; font-size: 40px; letter-spacing: 1px; }

  .address-field { position: absolute; background: var(--paper); border-radius: 0 28px 28px 0; display: flex; align-items: center; padding-left: 16px; letter-spacing: 0.5px; }
  .address-field--name { left: 66px; top: 112px; width: 246px; height: 71px; font-size: 43px; }
  .address-field--street { left: 62px; top: 196px; width: 248px; height: 69px; padding-left: 11px; font-size: 40px; }
  .address-field--city { left: 59px; top: 282px; width: 247px; height: 70px; padding-left: 8px; font-size: 42px; }
  .date-stamp { position: absolute; left: 62px; top: 381px; width: 151px; height: 99px; background: var(--paper); display: flex; align-items: center; justify-content: center; font-family: "Open Sans", sans-serif; font-weight: 400; font-size: 38px; }

  .brand-mark { position: absolute; left: 510px; top: 98px; width: 200px; height: 200px; border-radius: 50%; background: var(--honey-yellow); }
  .brand-name { position: absolute; left: 0; width: 1224px; top: 368px; text-align: center; color: var(--honey-yellow); font-family: "PT Sans", sans-serif; font-weight: 700; font-size: 46px; letter-spacing: 3px; }
  .brand-place { position: absolute; left: 0; width: 1224px; top: 456px; display: flex; justify-content: center; align-items: center; gap: 8px; font-family: "PT Sans", sans-serif; font-size: 20px; letter-spacing: 5px; }
  .brand-place::before, .brand-place::after { content: ""; width: 40px; height: 3px; background: var(--ink); }
  .product-name { position: absolute; left: 0; width: 1224px; top: 482px; text-align: center; font-size: 43px; line-height: 50px; letter-spacing: 0.5px; }

  .variety { position: absolute; left: 906px; width: 200px; top: 412px; text-align: center; font-size: 29px; }
  .weight { position: absolute; left: 906px; width: 200px; top: 456px; text-align: center; font-size: 43px; }
  .storage { position: absolute; left: 1120px; top: 50px; writing-mode: vertical-rl; font-size: 21px; line-height: 1; letter-spacing: 0.3px; white-space: nowrap; }
</style>
</head>
<body>
<div class="canvas">
  <section class="seal">
    <div class="seal-brand seal-brand--left">IMKEREI LINDNER</div>
    <p class="seal-text">SPRING BLOSOM<br>DAS BESTE AUS DER NATUR</p>
    <div class="seal-brand seal-brand--right">IMKEREI LINDNER</div>
  </section>

  <section class="label">
    <h2 class="best-before">MINDESTHALTBARKEITSDATUM</h2>

    <div class="address-field address-field--name">NAME</div>
    <div class="address-field address-field--street">STREET</div>
    <div class="address-field address-field--city">POST CITY</div>
    <div class="date-stamp">date</div>

    <div class="brand-mark"></div>
    <div class="brand-name">IMKEREI LINDNER</div>
    <div class="brand-place">LINDENTAL-AUE</div>
    <h1 class="product-name">FEINSTER BIENENHONIG</h1>

    <div class="variety">SPRING BLOSOM</div>
    <div class="weight">500G</div>
    <div class="storage">TROCKEN, DUNKEL UND VOR WÄRME GESCHÜTZT LAGERN</div>
  </section>
</div>
</body>
</html>
```